Social Media Graphics - Kestrel Climb

Create 6-7 individual social media graphics (square size) to encourage folks to join our online course, using either of the text below (only one set of text per graphic:

The Copperfield Ascent
How to Create a 7-Figure Business From Scratch
Sign Up Today!

Or

The Copperfield Ascent
Fast-track Your Way to a Multi-Million Business!
Sign Up Today!

For the color scheme of the graphics, use 1 or 2 colors in the color palette attached; or use any colors that look nice with their outfits; AVOID using red, white and blue altogether because it will look like an Independence Day (4th of July) graphic and we don’t want that; make sure the graphics appeal to both men and women

Make sure each graphic contains 1 of the 2 pics attached; and make sure one of the graphics is all TEXT only.

Target Market(s)

men and women looking to make more money

Industry/Entity Type

entrepreneurship

Requirements
Must have
• see the text document attached
Nice to have
• We are open to a nice color design; the color palette colors are not required, especially we don't want red, white and blue used together
Should not have
• AVOID using red, white and blue altogether because it will look like an Independence Day (4th of July) graphic and we dont want that

```html
<!DOCTYPE html>
<html lang="en">
<head>
<meta charset="utf-8">
<title>The Copperfield Ascent – Social Graphics</title>
<link href="https://fonts.googleapis.com/css2?family=Roboto:wght@400;500;700&display=swap" rel="stylesheet">
<style>
  :root {
    --board: #cbc3c3;
    --forest: #0f3f3a;
    --forest-deep: #0a2c29;
    --gold: #c8973a;
    --gold-light: #e2bd6e;
    --cream: #f7efe0;
    --sand: #f0dfc0;
    --ink: #1f1a14;
  }
  * { margin: 0; padding: 0; box-sizing: border-box; }
  html, body { width: 1200px; height: 855px; overflow: hidden; }
  body { background: var(--board); font-family: "Roboto", Arial, sans-serif; position: relative; }
  .tile { position: absolute; width: 332px; height: 332px; display: block; }
  .col-1 { left: 58px; } .col-2 { left: 434px; } .col-3 { left: 810px; }
  .row-1 { top: 63px; } .row-2 { top: 461px; }
  .tile text { font-family: "Roboto", Arial, sans-serif; }
  .brand { font-size: 20px; font-weight: 500; }
  .brand-light { font-size: 20px; font-weight: 400; }
  .headline { font-size: 24px; font-weight: 500; }
  .headline-bold { font-size: 24px; font-weight: 700; }
  .cta { font-size: 19px; font-weight: 700; }
  .feature-brand { font-size: 26px; font-weight: 400; letter-spacing: 1px; }
  .feature-headline { font-size: 46px; font-weight: 700; }
  .feature-cta { font-size: 22px; font-weight: 700; }
</style>
</head>
<body>

<svg width="0" height="0" style="position:absolute">
  <defs>
    <linearGradient id="hosts-dark" x1="0" y1="0" x2="0" y2="1">
      <stop offset="0" stop-color="#4a3a30"/><stop offset="0.5" stop-color="#2a2622"/><stop offset="1" stop-color="#24405e"/>
    </linearGradient>
    <linearGradient id="hosts-warm" x1="0" y1="0" x2="0" y2="1">
      <stop offset="0" stop-color="#5a4436"/><stop offset="0.55" stop-color="#a0705a"/><stop offset="1" stop-color="#231c18"/>
    </linearGradient>
  </defs>
</svg>

<!-- Tile 1: forest with gold badge -->
<svg class="tile col-1 row-1" viewBox="0 0 600 600" aria-label="Course graphic: How to Create a 7-Figure Business From Scratch">
  <rect width="600" height="600" fill="var(--forest)"/>
  <path d="M470 0 H600 V260 C590 140 540 60 470 0 Z" fill="var(--gold)"/>
  <circle cx="0" cy="0" r="118" fill="var(--cream)"/>
  <rect x="130" y="40" width="470" height="405" fill="url(#hosts-warm)" role="img" aria-label="Photo of the two course hosts smiling with arms crossed"/>
  <rect x="0" y="445" width="600" height="155" fill="var(--cream)"/>
  <path d="M0 463 H470" stroke="var(--forest)" stroke-width="3"/>
  <text class="brand" x="40" y="497" fill="var(--forest)">The Copperfield Ascent</text>
  <text class="headline" x="40" y="537" fill="#8a6220">How to Create a 7-Figure Business</text>
  <text class="headline" x="40" y="567" fill="#8a6220">From Scratch</text>
  <circle cx="548" cy="500" r="84" fill="var(--gold)"/>
  <circle cx="548" cy="500" r="72" fill="none" stroke="var(--cream)" stroke-width="2.5"/>
  <text class="cta" x="538" y="488" fill="var(--forest-deep)" text-anchor="middle">Sign Up</text>
  <text class="cta" x="538" y="512" fill="var(--forest-deep)" text-anchor="middle">Today!</text>
</svg>

<!-- Tile 2: gold glow with diagonal panel -->
<svg class="tile col-2 row-1" viewBox="0 0 600 600" aria-label="Course graphic: How to Create a 7-Figure Business From Scratch">
  <defs>
    <radialGradient id="glow-gold" cx="0.4" cy="0.15" r="0.6">
      <stop offset="0" stop-color="#fbf1d8"/><stop offset="0.6" stop-color="var(--gold-light)"/><stop offset="1" stop-color="var(--gold)"/>
    </radialGradient>
  </defs>
  <rect width="600" height="600" fill="url(#glow-gold)"/>
  <polygon points="528,0 600,0 600,425 475,425" fill="var(--forest)"/>
  <polygon points="0,200 45,600 0,600" fill="var(--cream)"/>
  <rect x="45" y="50" width="430" height="550" fill="url(#hosts-warm)" role="img" aria-label="Photo of the two course hosts smiling with arms crossed"/>
  <polygon points="255,425 600,425 600,600 160,600" fill="var(--cream)"/>
  <polygon points="232,425 255,425 160,600 138,600" fill="var(--forest)"/>
  <text class="brand" x="273" y="470" fill="var(--forest)">The Copperfield Ascent</text>
  <text class="headline" x="273" y="510" fill="#8a6220">How to Create a 7-Figure</text>
  <text class="headline" x="273" y="540" fill="#8a6220">Business From Scratch</text>
  <text class="cta" x="273" y="577" fill="var(--forest)">Sign Up Today!</text>
</svg>

<!-- Tile 3: header bands over gold -->
<svg class="tile col-3 row-1" viewBox="0 0 600 600" aria-label="Course graphic: Fast-track Your Way to a Multi-Million Business">
  <rect width="600" height="600" fill="var(--gold)"/>
  <rect x="0" y="0" width="600" height="95" fill="var(--forest)"/>
  <rect x="0" y="95" width="600" height="46" fill="var(--cream)"/>
  <text class="brand-light" x="300" y="33" fill="var(--cream)" text-anchor="middle">The Copperfield Ascent</text>
  <text class="headline-bold" x="300" y="72" fill="var(--cream)" text-anchor="middle">Fast-track Your Way to a Multi-Million Business!</text>
  <text class="cta" x="300" y="124" fill="var(--ink)" text-anchor="middle" font-weight="500">Sign Up Today!</text>
  <rect x="60" y="150" width="530" height="450" fill="url(#hosts-dark)" role="img" aria-label="Photo of the two course hosts in dark and denim outfits, arms crossed"/>
</svg>

<!-- Tile 4: curved header -->
<svg class="tile col-1 row-2" viewBox="0 0 600 600" aria-label="Course graphic: Fast-track Your Way to a Multi-Million Business">
  <rect width="600" height="600" fill="var(--gold)"/>
  <rect x="0" y="150" width="600" height="450" fill="url(#hosts-dark)" role="img" aria-label="Photo of the two course hosts in dark and denim outfits, arms crossed"/>
  <path d="M0 0 H600 V95 Q300 200 0 95 Z" fill="var(--forest)"/>
  <path d="M0 100 Q300 205 600 100" fill="none" stroke="var(--cream)" stroke-width="6"/>
  <text class="brand-light" x="300" y="33" fill="var(--cream)" text-anchor="middle">The Copperfield Ascent</text>
  <text class="headline-bold" x="300" y="77" fill="var(--cream)" text-anchor="middle">Fast-track Your Way to a Multi-Million Business!</text>
  <text class="cta" x="300" y="121" fill="var(--gold-light)" text-anchor="middle">Sign Up Today!</text>
</svg>

<!-- Tile 5: sand with forest circle -->
<svg class="tile col-2 row-2" viewBox="0 0 600 600" aria-label="Course graphic: Fast-track Your Way to a Multi-Million Business">
  <rect width="600" height="600" fill="var(--sand)"/>
  <circle cx="300" cy="110" r="185" fill="var(--forest)"/>
  <rect x="45" y="20" width="510" height="440" fill="url(#hosts-dark)" role="img" aria-label="Photo of the two course hosts in dark and denim outfits, arms crossed"/>
  <polygon points="0,420 180,450 0,470" fill="var(--gold)"/>
  <polygon points="0,470 600,400 600,415 0,485" fill="var(--cream)"/>
  <polygon points="0,485 600,415 600,600 0,600" fill="var(--forest)"/>
  <text class="brand-light" x="300" y="497" fill="var(--cream)" text-anchor="middle">The Copperfield Ascent</text>
  <text class="headline-bold" x="300" y="539" fill="var(--cream)" text-anchor="middle">Fast-track Your Way to a Multi-Million Business!</text>
  <text class="cta" x="300" y="580" fill="var(--gold-light)" text-anchor="middle">Sign Up Today!</text>
</svg>

<!-- Tile 6: text-only with diagonal bands -->
<svg class="tile col-3 row-2" viewBox="0 0 600 600" aria-label="Text-only course graphic: Fast-track Your Way to a Multi-Million Business">
  <rect width="600" height="600" fill="var(--forest-deep)"/>
  <polygon points="465,0 600,0 600,140 360,0" fill="var(--forest)"/>
  <polygon points="0,470 0,600 150,600" fill="var(--forest)"/>
  <polygon points="578,408 600,408 600,600 440,600" fill="var(--gold)"/>
  <polygon points="0,0 80,0 0,110" fill="var(--gold)"/>
  <text class="feature-brand" x="300" y="150" fill="var(--gold-light)" text-anchor="middle">The Copperfield Ascent</text>
  <rect x="250" y="172" width="100" height="3" fill="var(--gold)"/>
  <text class="feature-headline" x="300" y="248" fill="var(--cream)" text-anchor="middle">Fast-track Your</text>
  <text class="feature-headline" x="300" y="304" fill="var(--cream)" text-anchor="middle">Way to a</text>
  <text class="feature-headline" x="300" y="360" fill="var(--cream)" text-anchor="middle">Multi-Million</text>
  <text class="feature-headline" x="300" y="416" fill="var(--cream)" text-anchor="middle">Business!</text>
  <rect x="190" y="458" width="220" height="54" rx="27" fill="var(--gold)"/>
  <text class="feature-cta" x="300" y="493" fill="var(--forest-deep)" text-anchor="middle">Sign Up Today!</text>
</svg>

</body>
</html>
```